Sunset Harbour Living Web Page

We need a web page design that has two intro pages - first being a 'home page', then a link to the second page that has the 'content tabs' and a 'call to action' (see below).

The business helps people that wish to retire to S.E.Asia (Thailand, Malaysia, Indonesia,The Philippines etc) - to enjoy the lifestyle and the remaining years of their lives. What attracts S.E.Asia to many people is the lower cost, the atmoshpere and beauty of the tropics and the vibrancy of the various countries.

People that are wishing to make the most of their retirement and are adventurous at a great bargain compared to the cost of their own countries will be interested.

We help them achieve this - visa, financials (tax, gov't payments etc), introduce them to the right people for property, clubs, retirement facilities, insurance and so forth.

Therefore we are providing an extremely wide ranging service and this site will provide broad but general information only - with a call to action to come and see us for more specific information and how we can help them specifically.

This site will be predominantly for travel and lifestyle, it will be linked with another financial services (financial planning) site later down the track.

The colour scheme is dark green and blue - as per the attached logo design. Photos and background just think lifestyle and S.E.Asia - beaches/mountains/water/recreational activities for retirees.

Target market is mostly those coming up to retirement to those that are already retired. But we also expect to have some interest with younger people that would like to find out more and plan for the future. So a broad age group but I would say mostly 40-70 yrs old.

On the first (Home) page we would like our company name 'Sunset Harbour Living', our logo (which will be on all pages) and a statement such as: “Imagine a retirement where your dreams are brought to life, and you have never felt more alive. Let us show you how”. Then a link to the second page.

We would like an uncluttered site. On the second (contents) page the tabs would be:

- Visa
- Property
- Financials
- Travel
- Insurance & Healthcare
- Medical Tourism
- Cost of living
- Weekly Blogs and articles
- Sunset Harbour Living story

We would also like a call to action on the second page - asking them to leave their contact details if they wish to learn more or sign up to our weekly newsletter/blog.

We are open to suggestions and your imaginations.

Thank you
Gerald

Font styles to use
Serif
Script

Colors
0255a3
3377b5
00a990
9bcb3c
abd036
33b8a4
85abd2
cadf82
86cfc6

Requirements
Must have
• I have been asked by the web designer to receive a 'Web Font' so that we can 'get off of Plixora'. Hope that makes sense.

```html
<!DOCTYPE html>
<html lang="en">
<head>
<meta charset="utf-8">
<title>Sunset Harbour Living</title>
<link href="https://fonts.googleapis.com/css2?family=Oswald:wght@300;400;500&family=Raleway:wght@400;500;600;700&display=swap" rel="stylesheet">
<style>
  :root {
    --ink: #454545;
    --muted: #555555;
    --brand-blue: #0a9bd8;
    --brand-green: #13a84f;
    --rule: #cfcfcf;
    --white: #ffffff;
    --icon-grey: rgba(190, 190, 190, 0.85);
  }
  * { margin: 0; padding: 0; box-sizing: border-box; }
  html, body { width: 1200px; height: 750px; overflow: hidden; }
  body { font-family: "Raleway", sans-serif; color: var(--ink); background: #f3f1ee; }

  .home {
    position: relative;
    width: 1200px;
    height: 750px;
    overflow: hidden;
  }
  .backdrop {
    position: absolute;
    inset: 0;
    background:
      linear-gradient(180deg, rgba(255,255,255,0.55) 0%, rgba(255,255,255,0.35) 55%, rgba(245,225,220,0.45) 75%, rgba(255,255,255,0.5) 100%),
      linear-gradient(90deg, #e9eae6 0%, #dfe3da 40%, #e8e6df 100%);
  }
  .hero-photo {
    position: absolute;
    left: 568px;
    top: 0;
    width: 526px;
    height: 750px;
    background:
      linear-gradient(180deg, rgba(255,255,255,0) 80%, rgba(235,238,240,0.6) 100%),
      radial-gradient(ellipse at 60% 50%, #c9d2cf 0%, rgba(201,210,207,0) 60%),
      linear-gradient(180deg, #b9cc7e 0%, #d9dbb4 30%, #c8b39a 60%, #9fb0b6 85%, #b4c1c6 100%);
  }

  .brand {
    position: absolute;
    left: 131px;
    top: 128px;
    display: flex;
    align-items: center;
    gap: 10px;
  }
  .brand-mark {
    width: 30px;
    height: 30px;
    border-radius: 50%;
    background: var(--brand-green);
  }
  .brand-name {
    font-family: "Raleway", sans-serif;
    font-weight: 700;
    font-size: 22px;
    color: var(--brand-blue);
  }

  .tagline {
    position: absolute;
    left: 131px;
    top: 322px;
    font-family: "Oswald", sans-serif;
    font-weight: 300;
    font-size: 34px;
    line-height: 43.5px;
    color: var(--ink);
    letter-spacing: -0.2px;
  }
  .tagline strong { font-weight: 400; }

  .enter-button {
    position: absolute;
    left: 131px;
    top: 526px;
    width: 175px;
    height: 45px;
    background: var(--brand-blue);
    color: var(--white);
    display: flex;
    align-items: center;
    justify-content: center;
    gap: 15px;
    font-size: 19px;
    font-weight: 500;
    text-decoration: none;
    border-radius: 2px;
  }
  .enter-button svg { display: block; }

  .footer-rule {
    position: absolute;
    left: 131px;
    top: 693px;
    width: 382px;
    height: 1px;
    background: var(--rule);
  }
  .copyright {
    position: absolute;
    left: 131px;
    top: 711px;
    font-size: 14px;
    color: var(--muted);
  }
  .social {
    position: absolute;
    left: 859px;
    top: 707px;
    display: flex;
    align-items: center;
    gap: 7px;
    color: var(--white);
    font-size: 14px;
    font-weight: 500;
  }
  .social-label { margin-right: 6px; }
  .social-dot {
    width: 24px;
    height: 24px;
    border-radius: 50%;
    background: var(--icon-grey);
  }
</style>
</head>
<body>
  <main class="home">
    <div class="backdrop" role="img" aria-label="Soft, faded garden scene with a wooden bench"></div>
    <div class="hero-photo" role="img" aria-label="Smiling retired couple embracing on a wooden bench in a sunny garden"></div>

    <div class="brand">
      <span class="brand-mark"></span>
      <span class="brand-name">Sunset Harbour Living</span>
    </div>

    <h1 class="tagline">
      Imagine a retirement where<br>
      <strong>your Dreams</strong> are brought to life,<br>
      and you have never felt more alive.<br>
      <strong>Let us show you how</strong>
    </h1>

    <a class="enter-button" href="#">
      Enter Site
      <svg width="22" height="22" viewBox="0 0 22 22" aria-hidden="true">
        <circle cx="11" cy="11" r="11" fill="#ffffff"/>
        <path d="M9 6.5 L13.5 11 L9 15.5" fill="none" stroke="#0a9bd8" stroke-width="2.4" stroke-linecap="round" stroke-linejoin="round"/>
      </svg>
    </a>

    <div class="footer-rule"></div>
    <p class="copyright">© 2016 Sunsetharbour. Ltd. All Right Reserved</p>

    <div class="social">
      <span class="social-label">Follow us:</span>
      <span class="social-dot"></span>
      <span class="social-dot"></span>
      <span class="social-dot"></span>
      <span class="social-dot"></span>
    </div>
  </main>
</body>
</html>
```